Cyber Security firm requires new branding and website design

We are open to advice on project budget so feel free to message me regarding this. We understand there are people from all over the world looking at this so initially we may be looking at just a landing page to just give us an idea of the design and that can be enough to win this contest. From there we can agree a reward / payment for the whole site.
We're looking for a Designer with UI/UX and some branding skills. We really need someone to give us a direction and then create a mock-up in Photoshop. We have a great logo and so far our website has done the job but is very basic www.velquant.com . We can reuse most the content (and this can be used by the Designer) but we need a complete redesign. Keep it clear, simple, classy and uncluttered and we certainly need new color scheme.
I have attached our logo's and a copy of our business cards (the black logo is actually silver foil) to give you an idea of the sort of branding we like.
We are based in Los Angeles and our clients range from the Entertainment business and start-ups to Law and Financial firms so we need a site design that appeals to all of these sectors.
Once we have the design we can give it to our developer to turn into a working site.
Updates
I wasn't sure how this worked as its the first time I have used the site.
Happy to take feedback on what would be most attractive to you guys to get you to want to design for us.
Cheers
Dale
The styles we like personally tend to have blocks of content and some funky HTML 5 stuff (If you can design it we can code it). Here are some examples:
http://www.plumbo.co
http://quenlarfitnesshall.com/
http://grovemarkstudio.com/
We are a fun company and have a good sense of humor. Our client generally do too but they are also dealing with serious issues so if you can get something that's fun but puts across that we are serious about what we do that would be great. Oh and we love this one so if you can take some influence from this but keep it professional we would love to see it:
http://brightkettleworks.com/
I also like the old typewriter style lettering i have seen used on contact forms. However this has to be a cohesive design so we want you to add what looks right not just everything we like (unless you can do that well).
We understand that you show a static site so this is hard to demonstrate but we particularly like the videos people are embedding nowadays and would love to avoid stock photos where we can:
https://www.coinvanta.com/home
Hopefully this gives you all more food for thought.
Industry/Entity Type
Business
Colors
Designer to choose colors to be used in the design.
Look and feel
Each slider illustrates characteristics of the customer's brand and the style your logo design should communicate.

```html
<!DOCTYPE html>
<html lang="en">
<head>
<meta charset="utf-8">
<title>Velquant Security</title>
<link rel="stylesheet" href="https://fonts.googleapis.com/css2?family=Open+Sans:wdth,wght@75..100,300..800&display=swap">
<style>
:root{
  --ink:#1e1e1e;
  --text:#5a5a5a;
  --muted:#8a8a8a;
  --line:#d6d6d6;
  --paper:#ffffff;
  --band:#efefef;
  --card:#eeeeee;
  --header:#efefef;
  --btn:#4a4a4a;
  --btn-light:#a9a9a9;
  --footer:#262626;
  --footer-text:#c9c9c9;
  --footer-rule:#3c3c3c;
  --hero-dark:#06101f;
  --hero-mid:#123a66;
  --hero-light:#3d86c4;
}
*{box-sizing:border-box;margin:0;padding:0}
html,body{width:1200px;height:2639px;overflow:hidden}
body{position:relative;background:var(--paper);font-family:"Open Sans",Arial,sans-serif;color:var(--ink)}
.abs{position:absolute}
a{color:inherit;text-decoration:none}

/* header */
.site-header{left:0;top:0;width:1200px;height:141px;background:var(--header)}
.brand{left:120px;top:38px;display:flex;align-items:center;gap:12px}
.brand-mark{width:38px;height:38px;background:#6b6b6b}
.brand-name{font-size:21px;font-weight:600;letter-spacing:2px;color:#3a3a3a}
.header-mail{right:120px;top:26px;text-align:right;display:flex;gap:10px;align-items:center}
.header-mail small{display:block;font-size:12px;color:#555;line-height:14px}
.header-mail strong{display:block;font-size:14px;font-weight:600;color:#222}
.main-nav{right:120px;top:96px;display:flex;gap:34px;font-size:13px;color:#7a7a7a;text-transform:uppercase}
.main-nav .active{color:#111}

/* hero */
.hero{left:0;top:141px;width:1200px;height:477px;background:radial-gradient(ellipse at 50% 35%,var(--hero-light) 0%,var(--hero-mid) 38%,var(--hero-dark) 80%)}
.hero-arrow{top:360px}
.hero-title{right:122px;top:424px;text-align:right;font-stretch:75%;font-weight:700;font-size:36px;line-height:40px;color:#fff;text-transform:uppercase}
.hero-cta{left:966px;top:514px;width:112px;height:42px;background:var(--btn-light);color:#fff;font-stretch:75%;font-weight:700;font-size:17px;display:flex;align-items:center;justify-content:center;text-transform:uppercase}

/* welcome */
.welcome-media{left:120px;top:663px;width:244px;height:194px;background:linear-gradient(135deg,#e4e9ee,#b9c6d2)}
.welcome-title{left:389px;top:656px;font-size:24px;font-weight:700;text-transform:uppercase}
.welcome-text{left:389px;top:706px;width:690px;font-size:13.5px;line-height:22.5px;color:var(--text)}
.btn-outline{left:389px;top:816px;width:105px;height:39px;border:1px solid #c8c8c8;font-size:13px;color:#555;display:flex;align-items:center;justify-content:center;text-transform:uppercase}

/* reasons */
.reasons{left:0;top:901px;width:1200px;height:426px;background:var(--band)}
.reasons-title{left:0;top:944px;width:1200px;text-align:center;font-size:24px;font-weight:700;text-transform:uppercase}
.reason{width:290px}
.reason h3{display:flex;align-items:center;gap:8px;font-size:20px;font-weight:500;color:#222}
.reason p{margin-top:8px;font-size:12.5px;line-height:18px;color:var(--muted)}

/* services */
.section-title{left:0;width:1200px;text-align:center;font-size:40px;font-weight:300;text-transform:uppercase;color:#222}
.service{top:1457px;width:227px;height:195px;background:var(--card);text-align:center}
.service svg{margin-top:34px}
.service h3{margin-top:14px;font-size:17.5px;font-weight:600;color:#222}
.service p{margin-top:2px;font-size:13.5px;line-height:17px;color:var(--muted);padding:0 30px}

/* news */
.news{left:118px;top:1703px;width:962px;height:88px;border:1px solid var(--line)}
.news-date{left:0;top:0;width:62px;height:86px;background:#5b5b5b;color:#fff;text-align:center;text-transform:uppercase}
.news-date .m{display:block;margin-top:18px;font-size:15px;font-weight:600;line-height:16px}
.news-date .d{display:block;font-size:27px;font-weight:600;line-height:30px}
.news-title{left:91px;top:14px;font-size:15px;color:#222}
.news-excerpt{left:91px;top:40px;width:790px;font-size:12px;line-height:17px;color:var(--muted)}
.news-next{right:20px;top:26px}

/* videos */
.video{top:1918px;width:227px;height:144px}
.video svg{position:absolute;left:93px;top:52px}

/* jobs */
.jobs{left:0;top:2120px;width:1200px;height:146px;background:var(--band)}
.job-line{left:0;top:2151px;width:1200px;text-align:center;font-size:21px;color:#444}
.job-line small{font-size:12px}
.btn-dark{top:2190px;height:39px;background:var(--btn);color:#fff;font-size:14px;font-weight:600;display:flex;align-items:center;justify-content:center;text-transform:uppercase;border:2px solid #333}

/* footer */
.site-footer{left:0;top:2266px;width:1200px;height:373px;background:var(--footer);color:var(--footer-text)}
.contact-row{left:0;top:2298px;width:1200px;display:flex;justify-content:center;gap:28px;font-size:17px;color:#e8e8e8;align-items:center}
.contact-row span{display:flex;gap:8px;align-items:center}
.rule{left:0;width:1200px;height:1px;background:var(--footer-rule)}
.f-col h4{font-size:14px;font-weight:500;color:#eee;text-transform:uppercase;margin-bottom:8px}
.f-col ul{list-style:none;font-size:12px;line-height:22px;color:#a8a8a8}
.f-col li::before{content:"• ";color:#777}
.f-sep{top:2390px;width:1px;height:120px;background:var(--footer-rule)}
.newsletter-input{left:894px;top:2424px;width:186px;height:32px;background:#fff;display:flex;align-items:center;justify-content:space-between;padding-left:10px;font-size:12px;color:#777}
.newsletter-input b{width:40px;height:32px;background:#bdbdbd;display:flex;align-items:center;justify-content:center}
.social{top:2488px;width:20px;height:20px;background:#4a7fc8}
.legal{left:120px;top:2570px;font-size:11px;color:#cfcfcf;line-height:24px}
.round-btn{top:2578px;width:34px;height:34px;border:2px solid #cfcfcf;border-radius:50%;display:flex;align-items:center;justify-content:center}
</style>
</head>
<body>

<header class="abs site-header">
  <div class="abs brand"><span class="brand-mark"></span><span class="brand-name">VELQUANT SECURITY</span></div>
  <div class="abs header-mail">
    <div><small>E-mail</small><strong>support@velquant.com</strong></div>
    <svg width="26" height="20" viewBox="0 0 26 20"><rect width="26" height="20" fill="#888"/><path d="M0 0l13 11L26 0" fill="none" stroke="#efefef" stroke-width="2"/></svg>
  </div>
  <nav class="abs main-nav">
    <a class="active">Home</a><a>Penetration Testing</a><a>Staffing</a><a>Hot Jobs</a><a>News</a><a>About</a><a>Contact</a>
  </nav>
</header>

<section class="abs hero" role="img" aria-label="Wall of glowing blue data screens with streams of binary digits"></section>
<svg class="abs hero-arrow" style="left:20px" width="18" height="28" viewBox="0 0 18 28"><path d="M15 2L3 14l12 12" fill="none" stroke="#9aa6b4" stroke-width="3"/></svg>
<svg class="abs hero-arrow" style="left:1162px" width="18" height="28" viewBox="0 0 18 28"><path d="M3 2l12 12L3 26" fill="none" stroke="#9aa6b4" stroke-width="3"/></svg>
<h1 class="abs hero-title">Aliquam erat<br>volutpat</h1>
<a class="abs hero-cta">Contact us</a>

<div class="abs welcome-media" role="img" aria-label="Magnifying glass over a blue shield with a keyhole"></div>
<h2 class="abs welcome-title">Welcome to Velquant Security</h2>
<p class="abs welcome-text">Velquant Security is qualified penetration testing company assisting companies of all sizes to safeguard against an array of system breaches. Founded by a veteran team of dedicated ethical hackers with over 25 years of IT security experience, Velquant Security’s team ensures that your company’s IT network is thoroughly tested and safe-guarded against malicious attacks.</p>
<a class="abs btn-outline">Read more</a>

<section class="abs reasons"></section>
<h2 class="abs reasons-title">6 Reasons why your company needs an IT security audit</h2>

<div class="abs reason" style="left:130px;top:1030px"><h3><svg width="17" height="17" viewBox="0 0 17 17"><circle cx="8.5" cy="8.5" r="8.5" fill="#222"/><path d="M4.5 8.8l2.8 2.8 5.3-5.6" fill="none" stroke="#fff" stroke-width="2.2"/></svg>Focus</h3><p>Nearly every penetration test uncovers gaping security flaws and exploits that could cripple a company’s network.</p></div>
<div class="abs reason" style="left:464px;top:1030px"><h3><svg width="17" height="17" viewBox="0 0 17 17"><circle cx="8.5" cy="8.5" r="8.5" fill="#222"/><path d="M4.5 8.8l2.8 2.8 5.3-5.6" fill="none" stroke="#fff" stroke-width="2.2"/></svg>Zero Day Exploits</h3><p>Hackers have access to exploits which the software manufactures are unaware off and have not yet patched.</p></div>
<div class="abs reason" style="left:799px;top:1030px"><h3><svg width="17" height="17" viewBox="0 0 17 17"><circle cx="8.5" cy="8.5" r="8.5" fill="#222"/><path d="M4.5 8.8l2.8 2.8 5.3-5.6" fill="none" stroke="#fff" stroke-width="2.2"/></svg>Undetected Breaches</h3><p>Many companies do not even realize they have been compromised and may be leaking data for months or even years.</p></div>
<div class="abs reason" style="left:130px;top:1174px"><h3><svg width="17" height="17" viewBox="0 0 17 17"><circle cx="8.5" cy="8.5" r="8.5" fill="#222"/><path d="M4.5 8.8l2.8 2.8 5.3-5.6" fill="none" stroke="#fff" stroke-width="2.2"/></svg>Mobile Data Exposure</h3><p>Mobile devices are often unencrypted and vulnerable to theft or loss.</p></div>
<div class="abs reason" style="left:464px;top:1174px"><h3><svg width="17" height="17" viewBox="0 0 17 17"><circle cx="8.5" cy="8.5" r="8.5" fill="#222"/><path d="M4.5 8.8l2.8 2.8 5.3-5.6" fill="none" stroke="#fff" stroke-width="2.2"/></svg>Global Hacking</h3><p>International hackers are working round the clock to find new ways to breach systems.</p></div>
<div class="abs reason" style="left:799px;top:1174px"><h3><svg width="17" height="17" viewBox="0 0 17 17"><circle cx="8.5" cy="8.5" r="8.5" fill="#222"/><path d="M4.5 8.8l2.8 2.8 5.3-5.6" fill="none" stroke="#fff" stroke-width="2.2"/></svg>Cloud Security</h3><p>Companies making a move towards the cloud must understand the security risks and procedures.</p></div>

<h2 class="abs section-title" style="top:1380px">Our Services</h2>

<div class="abs service" style="left:118px">
  <svg width="56" height="50" viewBox="0 0 56 50"><path d="M8 34V26a20 20 0 0 1 40 0v8" fill="none" stroke="#222" stroke-width="6"/><rect x="4" y="28" width="12" height="20" rx="3" fill="#222"/><rect x="40" y="28" width="12" height="20" rx="3" fill="#222"/></svg>
  <h3>Emergency Response</h3><p>Contract Staffing</p>
</div>
<div class="abs service" style="left:363px">
  <svg width="56" height="50" viewBox="0 0 56 50"><circle cx="14" cy="13" r="7" fill="#222"/><circle cx="42" cy="13" r="7" fill="#222"/><circle cx="28" cy="18" r="8" fill="#222"/><path d="M2 36a12 10 0 0 1 24 0zM30 36a12 10 0 0 1 24 0z" fill="#222"/><path d="M14 48a14 13 0 0 1 28 0z" fill="#222"/></svg>
  <h3>Tactical</h3><p>Contingency permanent staffing</p>
</div>
<div class="abs service" style="left:608px">
  <svg width="56" height="50" viewBox="0 0 56 50"><circle cx="24" cy="20" r="14" fill="none" stroke="#222" stroke-width="6"/><path d="M34 30l12 12" stroke="#222" stroke-width="8" stroke-linecap="round"/></svg>
  <h3>Covert</h3><p>Executive Search</p>
</div>
<div class="abs service" style="left:853px">
  <svg width="56" height="50" viewBox="0 0 56 50"><circle cx="28" cy="25" r="22" fill="#222"/><path d="M17 14c6 2 4 8 9 9s2 8-2 12M34 9c-2 6 6 6 8 12s-5 6-4 12" fill="none" stroke="#eee" stroke-width="3"/></svg>
  <h3>Strategic</h3><p>Project outsourcing</p>
</div>

<article class="abs news">
  <div class="abs news-date"><span class="m">Jan</span><span class="d">22</span></div>
  <h3 class="abs news-title">Velquant Security founder to present at Media Safeguard Forum</h3>
  <p class="abs news-excerpt">In the last year, and specifically the last couple of weeks, a few high profile events have thrust content protection into the spotlight. Studio Media Services Guild (SMSG) and Digital Delivery Safety Council (DDSC)...</p>
  <svg class="abs news-next" width="20" height="34" viewBox="0 0 20 34"><path d="M3 3l14 14L3 31" fill="none" stroke="#aaa" stroke-width="3"/></svg>
</article>

<h2 class="abs section-title" style="top:1841px">Our Videos</h2>

<div class="abs video" style="left:118px;background:linear-gradient(135deg,#1a1a1f,#3b3a3d)" role="img" aria-label="Video: hands typing on a keyboard in low light">
  <svg width="40" height="40" viewBox="0 0 40 40"><circle cx="20" cy="20" r="19" fill="#bbb" fill-opacity=".85"/><path d="M15 12l13 8-13 8z" fill="#333"/></svg></div>
<div class="abs video" style="left:363px;background:linear-gradient(135deg,#0f2a33,#3b5b63 55%,#5a1616)" role="img" aria-label="Video: row of padlocks with one unlocked in red">
  <svg width="40" height="40" viewBox="0 0 40 40"><circle cx="20" cy="20" r="19" fill="#bbb" fill-opacity=".85"/><path d="M15 12l13 8-13 8z" fill="#333"/></svg></div>
<div class="abs video" style="left:608px;background:linear-gradient(135deg,#2e4e6c,#0f2238)" role="img" aria-label="Video: login screen with username and password fields">
  <svg width="40" height="40" viewBox="0 0 40 40"><circle cx="20" cy="20" r="19" fill="#bbb" fill-opacity=".85"/><path d="M15 12l13 8-13 8z" fill="#333"/></svg></div>
<div class="abs video" style="left:853px;background:linear-gradient(135deg,#2a0b12,#7a1e2a 50%,#1c0a10)" role="img" aria-label="Video: red warning sign over a circuit board">
  <svg width="40" height="40" viewBox="0 0 40 40"><circle cx="20" cy="20" r="19" fill="#bbb" fill-opacity=".85"/><path d="M15 12l13 8-13 8z" fill="#333"/></svg></div>

<section class="abs jobs"></section>
<p class="abs job-line">Trainee Recruitment Consultant - Velquant Security - Culver City, CA <small>(Jan 21, Full Time)</small></p>
<a class="abs btn-dark" style="left:459px;width:137px">Apply now</a>
<a class="abs btn-dark" style="left:603px;width:138px">View all jobs</a>

<footer class="abs site-footer"></footer>
<div class="abs contact-row">
  <span><svg width="12" height="16" viewBox="0 0 12 16"><path d="M2 1l3 0 1 4-2 1c1 3 2 4 4 5l1-2 3 1v3c-6 1-11-5-10-12z" fill="#e8e8e8"/></svg>Contact us today! +1 (424) 555-0187</span>
  <span style="color:#777">|</span>
  <span><svg width="12" height="16" viewBox="0 0 12 16"><path d="M6 0a6 6 0 0 1 6 6c0 4-6 10-6 10S0 10 0 6a6 6 0 0 1 6-6z" fill="#e8e8e8"/><circle cx="6" cy="6" r="2.2" fill="#262626"/></svg>Find our Location</span>
  <span style="color:#777">|</span>
  <span><svg width="16" height="12" viewBox="0 0 16 12"><rect width="16" height="12" fill="#e8e8e8"/><path d="M0 0l8 7 8-7" fill="none" stroke="#262626" stroke-width="1.5"/></svg>support@velquant.com</span>
</div>
<div class="abs rule" style="top:2354px"></div>

<div class="abs f-col" style="left:120px;top:2390px;width:260px">
  <h4>Navigation</h4>
  <div style="display:flex;gap:26px">
    <ul><li>Home</li><li>Penetration Testing</li><li>Staffing</li><li>Hot Jobs</li></ul>
    <ul><li>News</li><li>About</li><li>Contact</li></ul>
  </div>
</div>
<div class="abs f-sep" style="left:360px"></div>
<div class="abs f-col" style="left:399px;top:2390px"><h4>Staffing</h4><ul><li>Staffing Solutions</li><li>Healthcare InfoSec</li><li>Legal InfoSec</li><li>Start-up Infosec</li></ul></div>
<div class="abs f-sep" style="left:540px"></div>
<div class="abs f-col" style="left:568px;top:2390px;width:140px"><h4>About</h4><ul><li>About us</li><li style="line-height:16px;margin-top:3px">Corporate Social Responsibility</li></ul></div>
<div class="abs f-sep" style="left:708px"></div>
<div class="abs f-col" style="left:732px;top:2390px"><h4>Contact us</h4><ul><li>Contact us</li><li>Register a Vacancy</li><li>Submit a Resume</li></ul></div>
<div class="abs f-sep" style="left:872px"></div>
<div class="abs f-col" style="left:897px;top:2390px"><h4>Newsletter</h4></div>
<div class="abs newsletter-input">E-mail<b><svg width="14" height="16" viewBox="0 0 14 16"><path d="M1 1l12 7-12 7z" fill="#666"/></svg></b></div>
<div class="abs social" style="left:894px"></div>
<div class="abs social" style="left:925px;background:#4aa8e0"></div>

<div class="abs rule" style="top:2550px"></div>
<div class="abs legal">Home &nbsp;|&nbsp; Contact us &nbsp;|&nbsp; About us &nbsp;|&nbsp; Sitemap &nbsp;|&nbsp; Privacy Policy<br>Copyright &nbsp;© 2015 &nbsp;Velquant Security LLC. &nbsp;All rights reserved.</div>
<div class="abs round-btn" style="left:1003px"><svg width="16" height="12" viewBox="0 0 16 12"><rect width="16" height="12" fill="#e8e8e8"/><path d="M0 0l8 7 8-7" fill="none" stroke="#262626" stroke-width="1.5"/></svg></div>
<div class="abs round-btn" style="left:1046px"><svg width="14" height="16" viewBox="0 0 14 16"><path d="M7 15V2M1 8l6-6 6 6" fill="none" stroke="#cfcfcf" stroke-width="2"/></svg></div>

</body>
</html>
```